Copper Ridge Inquiries Letterhead

I would like to design a letterhead for a private investigation company. Our primary clients will be law firms. The business card is included below

```html
<!DOCTYPE html>
<html lang="en">
<head>
<meta charset="utf-8">
<title>Copper Ridge Inquiries Letterhead</title>
<link href="https://fonts.googleapis.com/css2?family=Open+Sans:wght@400;600;700&family=Montserrat:wght@500;600;700&display=swap" rel="stylesheet">
<style>
  :root {
    --navy: #1b3461;
    --orange: #ef5b2f;
    --body-grey: #7a7a7a;
    --ink: #2b2b2b;
    --paper: #ffffff;
  }
  * { box-sizing: border-box; margin: 0; padding: 0; }
  html, body { width: 999px; height: 1200px; overflow: hidden; background: var(--paper); }
  .letterhead { position: relative; width: 999px; height: 1200px; background: var(--paper); font-family: "Open Sans", sans-serif; }

  .brand { position: absolute; left: 68px; top: 92px; display: flex; align-items: center; gap: 14px; }
  .brand-dot { width: 44px; height: 44px; border-radius: 50%; background: var(--navy); }
  .brand-name { font-family: "Montserrat", sans-serif; font-weight: 700; font-size: 27px; color: var(--navy); letter-spacing: 0.2px; }

  .header-rule { position: absolute; left: 68px; top: 222px; width: 866px; height: 14px; }

  .sender { position: absolute; left: 84px; top: 302px; }
  .sender-name { font-size: 29px; font-weight: 600; color: var(--navy); line-height: 1.2; }
  .sender-title { font-size: 14px; color: var(--ink); margin-top: 1px; }
  .sender-details { list-style: none; margin-top: 8px; }
  .sender-details li { font-size: 17px; color: var(--ink); line-height: 24px; white-space: nowrap; }
  .sender-details .label { display: inline-block; width: 34px; color: var(--orange); font-weight: 600; }

  .letter-date { position: absolute; right: 79px; top: 414px; font-size: 17px; color: var(--ink); }

  .letter-body { position: absolute; left: 84px; top: 492px; width: 850px; }
  .letter-body p { font-size: 17.5px; color: var(--body-grey); line-height: 31.5px; margin-bottom: 30px; }
  .letter-body p span { display: block; white-space: nowrap; }

  .signoff { position: absolute; left: 700px; top: 858px; width: 190px; text-align: center; }
  .signature { width: 180px; height: 40px; margin: 0 auto 8px; border-radius: 4px; background: linear-gradient(90deg, #eef0f4, #e3e6ec); }
  .signoff-name { font-size: 16px; font-weight: 700; color: var(--ink); line-height: 18px; }
  .signoff-role { font-size: 16px; color: var(--ink); line-height: 18px; }

  .footer-block { position: absolute; left: 0; top: 1042px; width: 57px; height: 103px; background: var(--navy); }
  .footer-contacts { position: absolute; left: 68px; top: 1043px; list-style: none; }
  .footer-contacts li { display: flex; align-items: center; gap: 7px; height: 25.8px; font-family: "Montserrat", sans-serif; font-weight: 600; font-size: 13px; color: var(--navy); }
  .footer-contacts svg { width: 16px; height: 16px; flex: none; }
</style>
</head>
<body>
<main class="letterhead">
  <div class="brand">
    <span class="brand-dot"></span>
    <span class="brand-name">Copper Ridge Inquiries</span>
  </div>

  <svg class="header-rule" viewBox="0 0 866 14" aria-hidden="true">
    <polygon points="6,1 270,1 264,13 0,13" fill="var(--navy)"/>
    <rect x="262" y="5.5" width="604" height="2.5" fill="var(--orange)"/>
  </svg>

  <section class="sender">
    <h1 class="sender-name">Martin Hale</h1>
    <p class="sender-title">Chief Director</p>
    <ul class="sender-details">
      <li><span class="label">A :</span>12 Harlow Lane, Brookfield - 4021</li>
      <li><span class="label">W :</span>office@ridgemail.net, www.ridgeinquiries.net</li>
      <li><span class="label">P :</span>+555 - 01234 - 5678</li>
    </ul>
  </section>

  <p class="letter-date">Date, 10 September, 2019</p>

  <section class="letter-body">
    <p>
      <span>This is a sample letter that has been placed to demonstrate typing remat (Your Company). letterhead</span>
      <span>design. When positioned properly, it will serve to work in harmony with all other elements letterhead.</span>
      <span>This letterhead design is meant to project an image</span>
    </p>
    <p>
      <span>This letterhead design is meant project an image of professionalism reliability. By using simple aligen</span>
      <span>we have created a very spacious feeling. The simplicity suggest&nbsp; rengththe spaciousnes contributes h</span>
      <span>aesthetics the layout. These basic qualities along with the (Your Company)</span>
    </p>
    <p>
      <span>look and helps reinforce the (Your Company) brand. letterhead design is meant to project an image p</span>
      <span>design. When positioned properly, it will serve to work in harmony all the other elements letterhead.</span>
      <span>sionalism and reliability.</span>
    </p>
  </section>

  <div class="signoff">
    <div class="signature" role="img" aria-label="Handwritten signature of Daniel Pryce"></div>
    <p class="signoff-name">Daniel Pryce</p>
    <p class="signoff-role">Manager</p>
  </div>

  <div class="footer-block"></div>
  <ul class="footer-contacts">
    <li>
      <svg viewBox="0 0 16 16" aria-hidden="true"><circle cx="8" cy="8" r="8" fill="var(--orange)"/><path d="M5.3 4.2l1.4-.3.8 2-1 .8c.5 1 1.3 1.8 2.3 2.3l.8-1 2 .8-.3 1.4c-3.5.3-6.3-2.5-6-6z" fill="#fff"/></svg>
      555.014.2290
    </li>
    <li>
      <svg viewBox="0 0 16 16" aria-hidden="true"><circle cx="8" cy="8" r="8" fill="var(--orange)"/><path d="M8 3.5a3 3 0 0 0-3 3c0 2.2 3 5.8 3 5.8s3-3.6 3-5.8a3 3 0 0 0-3-3z" fill="#fff"/><circle cx="8" cy="6.5" r="1.1" fill="var(--orange)"/></svg>
      Granite Falls, CO
    </li>
    <li>
      <svg viewBox="0 0 16 16" aria-hidden="true"><circle cx="8" cy="8" r="8" fill="var(--orange)"/><circle cx="8" cy="6" r="2" fill="#fff"/><path d="M4.5 11.8c.4-1.8 1.8-2.8 3.5-2.8s3.1 1 3.5 2.8z" fill="#fff"/></svg>
      License No. 04471236
    </li>
    <li>
      <svg viewBox="0 0 16 16" aria-hidden="true"><circle cx="8" cy="8" r="8" fill="var(--orange)"/><text x="8" y="11.3" text-anchor="middle" font-family="Montserrat, sans-serif" font-weight="700" font-size="10" fill="#fff">@</text></svg>
      Owen@CopperRidgeInquiries.com
    </li>
  </ul>
</main>
</body>
</html>
```